Tincture Design for Woman Owned CBD Branf

LumiVera is a luxery CBD brand for millennial women.

Our premium L Oil contains 500mg of full spectrum CBD derived from specially-sourced hemp for unparalleled purity and quality. Each dropper delivers approximately 20mg of CBD. Available in two flavors, Natural and Mint.

The goal is to design an aesthetically pleasing tincture (bottle dropper) with label and box. The final design should coincide with our brand guidelines and easily marketed for beauty consumers. We are looking for a clean design, the use of raised fonts and/or metallic is fine.

We have 4 other designs we'd like to work on with the winning designer.

Target Market(s)

Millennial Women, Income $75k+

Font styles to use
Other font styles liked:
• See Branding Sheet

Requirements
Must have
• Must follow brand guidelines (see attached for colors, font, etc)
Nice to have
• Raised font or Metallic Print

```html
<!DOCTYPE html>
<html lang="en">
<head>
<meta charset="UTF-8">
<title>LumiVera Full Spectrum CBD – Tincture Label and Box</title>
<link rel="stylesheet" href="https://fonts.googleapis.com/css2?family=Italiana&family=Playfair+Display:wght@400;500&family=Montserrat:wght@500;600;800&family=Barlow:wght@400&family=Pathway+Gothic+One&display=swap">
<style>
  :root {
    --canvas: #d7d7d7;
    --white: #ffffff;
    --green: #1f6a58;
    --green-deep: #1b5b4b;
    --teal: #3aa58d;
    --gold: #c9a05a;
    --gold-deep: #b88c45;
    --gold-text: #c39a55;
    --ink-side: #1d1d1d;
  }
  * { box-sizing: border-box; margin: 0; padding: 0; }
  html, body {
    width: 1200px; height: 1200px; overflow: hidden;
    background: var(--canvas);
  }
  .canvas { position: relative; width: 1200px; height: 1200px; }

  /* shared pieces */
  .est {
    font-family: "Montserrat", sans-serif; font-weight: 500;
    color: var(--green); letter-spacing: 0.5em; text-align: center;
  }
  .brand-mark { display: flex; justify-content: center; margin: 0 auto; }
  .brand-mark span {
    display: block; border-radius: 50%; border: 1.5px solid var(--gold);
  }
  .brand-name {
    font-family: "Italiana", serif; font-weight: 400;
    color: var(--green); text-align: center; line-height: 1;
  }
  .tagline {
    font-family: "Montserrat", sans-serif; font-weight: 500;
    color: var(--gold-text); text-align: center; letter-spacing: 0.45em;
  }
  .white-zone { background: var(--white); }
  .gold-band { background: var(--gold); }
  .green-zone { background: var(--green); position: relative; }
  .absorption {
    font-family: "Barlow", sans-serif; color: var(--white);
    text-align: center; line-height: 1.2;
  }
  .dose-badge {
    background: var(--teal); border-radius: 50%;
    color: var(--white); text-align: center; margin: 0 auto;
    font-family: "Montserrat", sans-serif; font-weight: 800;
    display: flex; flex-direction: column; justify-content: center; line-height: 0.95;
  }
  .flavour {
    font-family: "Montserrat", sans-serif; font-weight: 800;
    color: var(--white); text-align: center; line-height: 1.2;
  }
  .supplement-tab {
    position: absolute; bottom: 0; left: 50%; transform: translateX(-50%);
    background: var(--gold); color: var(--white);
    font-family: "Playfair Display", serif; letter-spacing: 0.06em;
    text-align: center; border-radius: 14px 14px 0 0; white-space: nowrap;
  }

  /* bottle label */
  .bottle-label {
    position: absolute; left: 40px; top: 330px; width: 360px; height: 540px;
    display: flex; flex-direction: column;
  }
  .bottle-label .white-zone { height: 272px; padding-top: 58px; }
  .bottle-label .est { font-size: 10px; margin-bottom: 14px; }
  .bottle-label .brand-mark span { width: 22px; height: 22px; }
  .bottle-label .brand-name { font-size: 54px; margin-top: 16px; letter-spacing: 0.02em; }
  .bottle-label .tagline { font-size: 8.5px; margin-top: 22px; }
  .bottle-label .gold-band {
    height: 62px; display: flex; align-items: center; justify-content: center;
    border-bottom: 3px solid var(--white);
  }
  .bottle-label .gold-band h2 {
    font-family: "Playfair Display", serif; font-weight: 500;
    font-size: 30px; color: var(--white); letter-spacing: 0.02em;
  }
  .bottle-label .green-zone { flex: 1; padding-top: 14px; }
  .bottle-label .absorption { font-size: 14px; }
  .bottle-label .dose-badge { width: 170px; height: 72px; margin-top: 10px; font-size: 25px; }
  .bottle-label .dose-badge small { font-size: 21px; }
  .bottle-label .flavour { font-size: 15px; margin-top: 12px; }
  .bottle-label .supplement-tab { width: 220px; height: 40px; line-height: 42px; font-size: 15px; }

  /* box side panel */
  .box-side {
    position: absolute; left: 430px; top: 120px; width: 240px; height: 960px;
    display: flex; flex-direction: column;
  }
  .box-side .white-zone { height: 424px; padding: 56px 22px 0; }
  .box-side .est { font-size: 8px; margin-bottom: 10px; }
  .box-side .brand-mark span { width: 18px; height: 18px; }
  .box-side .brand-name { font-size: 34px; margin-top: 12px; }
  .box-side .tagline { font-size: 6px; margin-top: 14px; letter-spacing: 0.3em; }
  .side-copy {
    font-family: "Pathway Gothic One", sans-serif; color: var(--ink-side);
    font-size: 14.5px; line-height: 1.45; text-align: justify; margin-top: 30px;
  }
  .box-side .gold-band {
    height: 176px; display: flex; align-items: center; justify-content: center; gap: 18px;
    border-bottom: 4px solid var(--white);
  }
  .badge-seal { width: 84px; height: 84px; border-radius: 50%; border: 3px solid var(--white); }
  .box-side .green-zone { flex: 1; padding: 26px 20px 0; }
  .side-copy.light { color: var(--white); text-align: center; margin-top: 0; font-size: 14px; }
  .side-copy.light + .side-copy.light { margin-top: 26px; }
  .fda-box {
    border: 1.5px solid var(--white); margin-top: 30px; padding: 10px 8px;
    font-family: "Pathway Gothic One", sans-serif; color: var(--white);
    font-size: 12.5px; text-align: center; line-height: 1.45;
  }
  .box-side .supplement-tab { width: 180px; height: 40px; line-height: 42px; font-size: 14px; }

  /* box front panel */
  .box-front {
    position: absolute; left: 670px; top: 120px; width: 490px; height: 960px;
    display: flex; flex-direction: column;
  }
  .box-front .white-zone { height: 424px; padding-top: 126px; }
  .box-front .est { font-size: 12px; margin-bottom: 18px; }
  .box-front .brand-mark span { width: 28px; height: 28px; }
  .box-front .brand-name { font-size: 74px; margin-top: 24px; letter-spacing: 0.02em; }
  .box-front .tagline { font-size: 11px; margin-top: 30px; }
  .box-front .gold-band {
    height: 176px; border-bottom: 4px solid var(--white);
    display: flex; flex-direction: column; align-items: center; justify-content: center;
  }
  .box-front .gold-band .kicker {
    font-family: "Playfair Display", serif; font-weight: 500;
    color: var(--white); font-size: 26px; letter-spacing: 0.02em;
  }
  .box-front .gold-band .headline {
    font-family: "Playfair Display", serif; font-weight: 400;
    color: var(--white); font-size: 108px; line-height: 0.95; letter-spacing: 0.02em;
  }
  .box-front .green-zone { flex: 1; padding-top: 30px; }
  .box-front .absorption { font-size: 24px; }
  .box-front .dose-badge { width: 196px; height: 92px; margin-top: 26px; font-size: 32px; }
  .box-front .dose-badge small { font-size: 27px; }
  .box-front .flavour { font-size: 20px; margin-top: 30px; }
  .box-front .supplement-tab { width: 280px; height: 52px; line-height: 54px; font-size: 20px; }
</style>
</head>
<body>
<main class="canvas">

  <section class="bottle-label" aria-label="Bottle label">
    <div class="white-zone">
      <p class="est">EST. 2020</p>
      <div class="brand-mark"><span></span></div>
      <h1 class="brand-name">LUMIVERA</h1>
      <p class="tagline">PREMIUM CBD PRODUCTS</p>
    </div>
    <div class="gold-band"><h2>FULL SPECTRUM CBD</h2></div>
    <div class="green-zone">
      <p class="absorption">10X Greater Absorption<br>THAN CBD OILS</p>
      <div class="dose-badge">500MG<small>THC FREE</small></div>
      <p class="flavour">MINT FLAVOUR</p>
      <div class="supplement-tab">DIETARY SUPPLEMENT</div>
    </div>
  </section>

  <section class="box-side" aria-label="Box side panel">
    <div class="white-zone">
      <p class="est">EST. 2020</p>
      <div class="brand-mark"><span></span></div>
      <h2 class="brand-name">LUMIVERA</h2>
      <p class="tagline">PREMIUM CBD PRODUCTS</p>
      <p class="side-copy">Do not exceed suggested use. Pregnant or nursing women should consult a physician before using this product. Individuals who have a health condition or are taking medication(s) should check with their physician before use. Immediately discontinue use and consult your physician if any adverse reactions seem to occur. Always check with a physician before starting any dietary supplement regimen.</p>
    </div>
    <div class="gold-band">
      <div class="badge-seal" role="img" aria-label="Cruelty free badge"></div>
      <div class="badge-seal" role="img" aria-label="Pharmacist owned brand badge"></div>
    </div>
    <div class="green-zone">
      <p class="side-copy light">STORE IN A COOL, DARK PLACE. KEEP BOTTLE TIGHTLY CLOSED. KEEP OUT OF THE REACH OF CHILDREN.</p>
      <p class="side-copy light">SUGGESTED USE: One serving (1 dropper) per day. See VeraDrops.com for more suggestions.</p>
      <p class="fda-box">These statements have not been evaluated by the US Food and Drug Administration. This product is not intended to diagnose, treat, cure or prevent any disease.</p>
      <div class="supplement-tab">DIETARY SUPPLEMENT</div>
    </div>
  </section>

  <section class="box-front" aria-label="Box front panel">
    <div class="white-zone">
      <p class="est">EST. 2020</p>
      <div class="brand-mark"><span></span></div>
      <h2 class="brand-name">LUMIVERA</h2>
      <p class="tagline">PREMIUM CBD PRODUCTS</p>
    </div>
    <div class="gold-band">
      <p class="kicker">FULL SPECTRUM</p>
      <p class="headline">CBD</p>
    </div>
    <div class="green-zone">
      <p class="absorption">10X Greater Absorption<br>THAN CBD OILS</p>
      <div class="dose-badge">500MG<small>THC FREE</small></div>
      <p class="flavour">MINT FLAVOUR</p>
      <div class="supplement-tab">DIETARY SUPPLEMENT</div>
    </div>
  </section>

</main>
</body>
</html>
```